Harborline Stay Collective Business Card Design

Design a business card for Harborline Stay Collective. Look at the website for colors and reference. Card should have logo, name, title, office number, mobile number, email, URL and a tagline like, "Luxury Hotel & Resort Email Marketing" (This might change).

https://www.harborlinestaycollective.net

The rest I will leave up to your imagination.

Contact Information for Business Card

Logo, name, title, office number, mobile number, email, URL and a tagline like, "Luxury Hotel & Resort Email Marketing" (This might change).

```html
<!DOCTYPE html>
<html lang="en">
<head>
<meta charset="utf-8">
<title>Harborline Stay Collective – Business Card</title>
<link rel="stylesheet" href="https://fonts.googleapis.com/css2?family=Jost:wght@400;500;700&family=Marcellus&display=swap">
<style>
  :root {
    --page-bg: #b8b8b9;
    --card-dark: #121618;
    --photo-forest: #1d2a1f;
    --photo-sea: #0f3338;
    --photo-sky: #151a1e;
    --accent: #f07d12;
    --text-light: #ffffff;
  }
  * { margin: 0; padding: 0; box-sizing: border-box; }
  html, body {
    width: 1200px; height: 1200px; overflow: hidden;
    background: var(--page-bg);
  }
  .canvas { position: relative; width: 1200px; height: 1200px; }
  .card {
    position: absolute; left: 206px; width: 788px; height: 450px;
    background: var(--card-dark); overflow: hidden;
    color: var(--text-light);
    font-family: "Jost", sans-serif;
  }
  .card--front { top: 96px; }
  .card--back { top: 650px; }
  .card__photo {
    position: absolute; inset: 0;
    background:
      linear-gradient(180deg, var(--photo-sky) 0%, transparent 26%),
      linear-gradient(100deg, var(--photo-forest) 0%, #1a2620 38%, var(--photo-sea) 62%, #112a2e 100%);
    opacity: 0.9;
  }
  .card__shade { position: absolute; inset: 0; background: rgba(10, 12, 14, 0.45); }
  .brand {
    position: absolute; left: 43px; top: 48px;
    display: flex; align-items: center; gap: 12px;
    font-family: "Jost", sans-serif; font-weight: 700;
    font-size: 25px; letter-spacing: 0.5px; text-transform: uppercase;
    color: var(--text-light);
  }
  .brand__mark { width: 18px; height: 18px; background: var(--accent); }
  .person { position: absolute; left: 43px; top: 188px; }
  .person__name {
    font-family: "Marcellus", serif; font-weight: 400;
    font-size: 39px; color: var(--accent); line-height: 1.1;
  }
  .person__title { font-size: 19px; margin-top: 6px; }
  .contact {
    position: absolute; top: 322px;
    font-size: 23px; line-height: 30px; list-style: none;
  }
  .contact--direct { left: 43px; }
  .contact--office { left: 451px; }
  .tagline {
    position: absolute; left: 0; right: 0; top: 202px; text-align: center;
    font-family: "Marcellus", serif; font-size: 30px; color: var(--accent);
  }
  .website {
    position: absolute; left: 0; right: 0; top: 386px; text-align: center;
    font-size: 19px;
  }
</style>
</head>
<body>
<main class="canvas">
  <section class="card card--front">
    <div class="card__photo" role="img" aria-label="Coastal photograph of forested headland cliffs above a turquoise sea"></div>
    <div class="card__shade"></div>
    <div class="brand"><span class="brand__mark"></span>Harborline Stay Collective</div>
    <div class="person">
      <h1 class="person__name">Daniel Brooks</h1>
      <p class="person__title">CEO &amp; Founder</p>
    </div>
    <ul class="contact contact--direct">
      <li>482 730 615</li>
      <li>482 730 629</li>
      <li>daniel@harborlinestay.net</li>
    </ul>
    <ul class="contact contact--office">
      <li>14 Marlow Street,</li>
      <li>West Harborview</li>
      <li>5810 VA</li>
    </ul>
  </section>

  <section class="card card--back">
    <div class="card__photo" role="img" aria-label="Coastal photograph of forested headland cliffs above a turquoise sea"></div>
    <div class="card__shade"></div>
    <p class="tagline">Luxury Hotel &amp; Resort Email Marketing</p>
    <p class="website">www.harborlinestaycollective.net</p>
  </section>
</main>
</body>
</html>
```